UX interface for a Crypto currency payment gateway

This project requires you to open an account on our development web site http://dev.quorvan.com/cgi-bin/d

It requires you, as well, to download and install a Bitcoin client working on the testnet network (such as electrum), then get some Bitcoin testnet (those are free for who knows how to get them). "Simulate a payment" works as well.

This project requires you to know how to work with Bitcoins and cryptocurrencies.

Do NOT submit work if you're not interested in crypto-currencies.

Then, make some simulated payments on our development web site (Bitcoin testnet is only one supported crypto-currency there) to fill up a little bit the transaction report and the wallets.

Our UX sucks, yep, I know that, that's why we need you !

Then propose a design for the back office, first page is good enough (Accounts & Wallets).

You can change the layout as you see fit, the contest is as much about the UX design than the graphic design.

The price of the contest is for the best design of the first page only (Accounts & Wallets).

However, the winner will be required to code his design in HTML/CSS (JS may be required as well depending on your design) and he will get the whole back office and check out page to design and code in a one to one relationship with the customer (be prepared for a long term project). The winner will integrate his coding inside our templates.

Do NOT submit work if you're not interested to take the whole project or if you're not able to dedicate enough time to deliver a big quantity of work fast.

Number of Pages Required

1 page

Font styles to use
Sans Serif

Requirements
Must have
• Design must look professional in "bank" style.

```html
<!DOCTYPE html>
<html lang="en">
<head>
<meta charset="utf-8">
<title>LedgerGate – Accounts &amp; Wallet</title>
<link rel="stylesheet" href="https://fonts.googleapis.com/css2?family=Montserrat:wght@400;500;600&display=swap">
<style>
  :root {
    --page-bg: #1f2535;
    --brand-bg: #1f2533;
    --topbar-bg: #0b0f1a;
    --accent-yellow: #f2c200;
    --nav-green: #4ea86a;
    --nav-top: #17b9f2;
    --nav-bottom: #2a6cf0;
    --nav-section: rgba(18, 90, 170, 0.45);
    --tab-bg: #262c3a;
    --tab-border: #4a5061;
    --panel-bg: #ffffff;
    --title-left: #2a7bd6;
    --title-right: #4c90e2;
    --head-bg: #4d535b;
    --stripe: #e2eee6;
    --cell-line: #e4e6ea;
    --text-dark: #2b2f36;
    --text-light: #ffffff;
  }
  * { box-sizing: border-box; margin: 0; padding: 0; }
  html, body {
    width: 1200px; height: 802px; overflow: hidden;
    background: var(--page-bg);
    font-family: 'Montserrat', sans-serif;
    color: var(--text-light);
  }
  .app { position: relative; width: 1200px; height: 802px; }

  .brand {
    position: absolute; left: 0; top: 0; width: 240px; height: 88px;
    background: var(--brand-bg);
    display: flex; align-items: center; justify-content: center; gap: 8px;
    font-size: 16px; font-weight: 500; letter-spacing: 0.5px;
  }
  .brand-dot { width: 10px; height: 10px; border-radius: 50%; background: var(--text-light); }
  .topbar {
    position: absolute; left: 240px; top: 0; width: 960px; height: 88px;
    background: var(--topbar-bg);
  }
  .top-icons { position: absolute; right: 40px; top: 32px; display: flex; gap: 21px; }
  .top-icons svg { width: 24px; height: 24px; stroke: var(--accent-yellow); fill: none; stroke-width: 1.8; stroke-linecap: round; stroke-linejoin: round; }

  .sidenav {
    position: absolute; left: 46px; top: 120px; width: 184px; height: 587px;
    background: linear-gradient(180deg, var(--nav-top) 0%, #1e9af0 45%, var(--nav-bottom) 100%);
    border-radius: 4px 0 0 4px; overflow: hidden;
  }
  .nav-head {
    height: 38px; background: var(--nav-green);
    font-size: 15px; font-weight: 500; display: flex; align-items: center; padding-left: 23px;
  }
  .nav-section {
    height: 43px; background: var(--nav-section);
    font-size: 14px; font-weight: 500; display: flex; align-items: center; padding-left: 31px;
  }
  .nav-item {
    height: 41px; font-size: 11px; display: flex; align-items: center; padding-left: 31px;
    border-bottom: 1px solid rgba(255,255,255,0.12);
  }
  .nav-item.plain { border-bottom: none; }
  .nav-item svg { width: 13px; height: 13px; margin-left: 10px; stroke: #fff; fill: none; stroke-width: 1.6; }
  .nav-label {
    margin: 2px 6px 6px 6px; height: 37px; border: 1.5px solid #fff;
    font-size: 12px; display: flex; align-items: center; padding-left: 24px;
  }

  .tabs { position: absolute; left: 240px; top: 122px; display: flex; gap: 9px; }
  .tab {
    height: 36px; background: var(--tab-bg); border: 1px solid var(--tab-border); border-bottom: none;
    font-size: 13.5px; display: flex; align-items: center; justify-content: center;
  }
  .tab-paid { width: 115px; }
  .tab-send { width: 145px; }

  .panel {
    position: absolute; left: 230px; top: 158px; width: 927px; height: 548px;
    background: var(--panel-bg);
  }
  .data-card { position: absolute; left: 12px; border: 1px solid var(--cell-line); }
  .wallets { top: 16px; }
  .transactions { top: 247px; }
  .card-title {
    height: 30px; background: linear-gradient(90deg, var(--title-left), var(--title-right));
    font-size: 13px; font-weight: 500; display: flex; align-items: center; padding-left: 17px;
  }
  table { border-collapse: collapse; table-layout: fixed; }
  th {
    height: 30px; background: var(--head-bg); text-align: left;
    font-size: 11.5px; font-weight: 600; padding-left: 34px; color: var(--text-light);
  }
  td {
    height: 30.5px; font-size: 9.6px; color: var(--text-dark); padding-left: 34px;
    border-left: 1px solid var(--cell-line);
  }
  td:first-child { border-left: none; }
  tr:nth-child(even) td { background: var(--stripe); }

  .footer {
    position: absolute; left: 0; top: 751px; width: 1200px; text-align: center;
    font-size: 13px; color: var(--text-light);
  }
</style>
</head>
<body>
<div class="app">
  <div class="brand"><span class="brand-dot"></span>LedgerGate</div>
  <header class="topbar">
    <div class="top-icons">
      <svg viewBox="0 0 24 24" aria-label="Notifications"><path d="M6 17V11a6 6 0 0 1 12 0v6l2 2H4z"/><path d="M10 21h4"/><circle cx="17" cy="6" r="2.5"/></svg>
      <svg viewBox="0 0 24 24" aria-label="Profile"><circle cx="12" cy="12" r="10"/><circle cx="12" cy="9" r="3.5"/><path d="M6 18c1.5-3 10.5-3 12 0"/></svg>
      <svg viewBox="0 0 24 24" aria-label="Log out"><path d="M14 4H5v16h9"/><path d="M14 8v-4M14 20v-4"/><path d="M10 12h11M18 9l3 3-3 3"/></svg>
    </div>
  </header>

  <nav class="sidenav">
    <div class="nav-head">Accounts &amp; Wallet</div>
    <div class="nav-section">Get Paid</div>
    <div class="nav-item">Simulate a Payment</div>
    <div class="nav-item">Generate Invoice</div>
    <div class="nav-item plain">Upload Invoice</div>
    <div class="nav-section">Accounts</div>
    <div class="nav-item plain">Martin J Corwell
      <svg viewBox="0 0 14 14"><path d="M6 2H2v10h10V8"/><path d="M5 9l1-3 5-5 2 2-5 5z"/></svg>
    </div>
    <div class="nav-label">Label</div>
    <div class="nav-item plain">Record New Account</div>
  </nav>

  <div class="tabs">
    <div class="tab tab-paid">Get Paid</div>
    <div class="tab tab-send">Send &amp; Receive</div>
  </div>

  <main class="panel">
    <section class="data-card wallets">
      <div class="card-title">WALLETS</div>
      <table>
        <colgroup><col style="width:120px"><col style="width:122px"><col style="width:98px"><col style="width:131px"></colgroup>
        <tr><th>Currency</th><th>Balance</th><th style="padding-left:35px">USD</th><th>More...</th></tr>
        <tr><td>BTC</td><td>0.000000</td><td>0.00</td><td>Topup Wallet</td></tr>
        <tr><td>BTCtestnet</td><td>0.000000</td><td>0.00</td><td>Topup Wallet</td></tr>
        <tr><td>ETH</td><td>0.000000</td><td>0.00</td><td>Topup Wallet</td></tr>
        <tr><td>LTC</td><td>0.000000</td><td>0.00</td><td>Topup Wallet</td></tr>
        <tr><td>LTCtestnet</td><td>0.000000</td><td>0.00</td><td>Topup Wallet</td></tr>
      </table>
    </section>

    <section class="data-card transactions">
      <div class="card-title">RESENT TRANSACTIONS</div>
      <table>
        <colgroup><col style="width:120px"><col style="width:122px"><col style="width:98px"><col style="width:122px"><col style="width:119px"><col style="width:138px"><col style="width:115px"></colgroup>
        <tr><th>Date</th><th>Customer</th><th>Invoice #</th><th>Received</th><th>Amount</th><th>Exchange rate</th><th>Info</th></tr>
        <tr><td>02.05.2018</td><td>Name Here</td><td>01568</td><td>Name Here</td><td>58203.220</td><td>-256.00</td><td>Pending</td></tr>
        <tr><td>30.04.2018</td><td>Name Here</td><td>01556</td><td>Name Here</td><td>48203.220</td><td>-12.600</td><td>Process</td></tr>
        <tr><td>28.04.2018</td><td>Name Here</td><td>01252</td><td>Name Here</td><td>68203.220</td><td>-156.00</td><td>Completed</td></tr>
        <tr><td>15.04.2018</td><td>Name Here</td><td>02680</td><td>Name Here</td><td>28203.220</td><td>+556.00</td><td>Pending</td></tr>
        <tr><td>09.04.2018</td><td>Name Here</td><td>01568</td><td>Name Here</td><td>98203.220</td><td>-256.00</td><td>Completed</td></tr>
      </table>
    </section>
  </main>

  <footer class="footer">© COPYRIGHT 2018. LEDGERGATE. ALL RIGHTS RESERVED.</footer>
</div>
</body>
</html>
```